Pruett Family Motto/Mission Statement

We are creating a poster to be hung in our home with several purpose statements for our family (last name Pruett, and "The Pruett Family" should be included in the poster prominently). The text that we want included is in the attached file.

Our kids range in age from 8 to 17, so we are looking for something that is homey and cheerful, but fairly bold and oriented to older kids (and not so much younger kids).

I've attached a couple of example poster/statements that we generally like. Overall color scheme could include blues and greens and possibly some brown.

Anticipated size of this poster would be 18"x24" with a portrait orientation.

```html
<!DOCTYPE html>
<html lang="en">
<head>
<meta charset="utf-8">
<title>The Pruett Family</title>
<link rel="stylesheet" href="https://fonts.googleapis.com/css2?family=EB+Garamond:wght@500&family=Roboto+Condensed:wght@400;700;900&display=swap">
<style>
  :root {
    --page: #eae8e9;
    --frame: #1e1b19;
    --ink-title: #0d4c9a;
    --white: #ffffff;
    --sky: #71c2ee;
    --azure: #4db6ea;
    --cyan: #00a5e0;
    --cerulean: #0494d9;
    --ocean: #0576c0;
    --cobalt: #0861a8;
    --navy: #0e3f8a;
  }
  * { box-sizing: border-box; margin: 0; padding: 0; }
  html, body { width: 1200px; height: 1000px; overflow: hidden; background: var(--page); }
  body { position: relative; font-family: "Roboto Condensed", "Arial Narrow", sans-serif; color: var(--white); }

  .poster {
    position: absolute; left: 253px; top: 38px; width: 694px; height: 925px;
    background: var(--frame); overflow: hidden;
    box-shadow: 4px 6px 10px rgba(0,0,0,.25);
  }
  .panel { position: absolute; overflow: hidden; }
  .statement { position: absolute; font-size: 33px; line-height: 33px; letter-spacing: -0.2px; }
  .statement b { font-weight: 700; }

  .title-panel { left: 20px; top: 19px; width: 388px; height: 170px; background: var(--white); color: var(--ink-title); font-family: "EB Garamond", Georgia, serif; font-weight: 500; text-align: center; z-index: 2; }
  .title-row { position: absolute; left: 50px; width: 288px; display: flex; align-items: center; gap: 8px; }
  .title-row::before, .title-row::after { content: ""; flex: 1; height: 1.5px; background: var(--ink-title); }
  .title-the { top: 20px; font-size: 25px; letter-spacing: 2px; }
  .title-name { position: absolute; left: 0; right: 0; top: 43px; font-size: 70px; line-height: 80px; letter-spacing: 1px; }
  .title-family { top: 120px; font-size: 23px; letter-spacing: 2px; }

  .adventure { left: 413px; top: 19px; width: 262px; height: 349px; background: var(--sky); }
  .learn { left: 20px; top: 194px; width: 388px; height: 174px; background: var(--azure); }
  .kindness { left: 20px; top: 373px; width: 388px; height: 178px; background: var(--cyan); }
  .fit { left: 413px; top: 373px; width: 262px; height: 178px; background: var(--cerulean); }
  .right-thing { left: 20px; top: 556px; width: 262px; height: 348px; background: var(--ocean); }
  .humor { left: 287px; top: 556px; width: 388px; height: 172px; background: var(--cobalt); }
  .positive { left: 287px; top: 733px; width: 388px; height: 171px; background: var(--navy); }

  .figure-slot { position: absolute; border-radius: 6px; background: rgba(255,255,255,.28); }

  .watermark {
    position: absolute; left: 20px; top: 194px; width: 655px; height: 710px; overflow: hidden; pointer-events: none;
    font-weight: 900; color: rgba(255,255,255,.18); text-transform: uppercase; z-index: 1;
  }
  .watermark span {
    position: absolute; display: block; font-size: 130px; line-height: 130px;
    transform-origin: left top; transform: rotate(-90deg); white-space: nowrap;
  }
  .statement, .poster svg, .figure-slot { z-index: 2; }
</style>
</head>
<body>
  <main class="poster">
    <section class="panel title-panel">
      <div class="title-row title-the">THE</div>
      <div class="title-name">PRUETT</div>
      <div class="title-row title-family">FAMILY</div>
    </section>

    <section class="panel adventure">
      <div class="figure-slot" role="img" aria-label="Line icon of a hiker climbing a steep slope" style="left:56px;top:32px;width:142px;height:120px;"></div>
      <p class="statement" style="left:0;right:0;top:164px;text-align:center;">We create<br><b>adventure</b><br>and choose<br>experiences<br>over things</p>
    </section>

    <section class="panel learn">
      <p class="statement" style="left:36px;top:36px;">We <b>love</b><br>to learn<br>new things.</p>
      <svg style="position:absolute;left:230px;top:50px;" width="100" height="72" viewBox="0 0 100 72" fill="none" stroke="#fff" stroke-width="2.5" stroke-linejoin="round">
        <path d="M50 12 C38 4 18 4 6 8 V62 C18 58 38 58 50 66 C62 58 82 58 94 62 V8 C82 4 62 4 50 12 Z"/>
        <path d="M50 12 V66"/>
        <path d="M2 14 V68 C18 64 38 64 50 70 C62 64 82 64 98 68 V14"/>
      </svg>
    </section>

    <section class="panel kindness">
      <svg style="position:absolute;left:34px;top:36px;" width="40" height="102" viewBox="0 0 40 102" fill="none" stroke="#fff" stroke-width="2.5">
        <path d="M20 4 C14 14 11 20 11 25 a9 9 0 0 0 18 0 C29 20 26 14 20 4 Z"/>
        <path d="M20 36 V44"/>
        <rect x="4" y="44" width="32" height="54" rx="4"/>
      </svg>
      <p class="statement" style="left:105px;top:45px;"><b>Kindness</b><br>guides our words<br>and deeds.</p>
    </section>

    <section class="panel fit">
      <p class="statement" style="left:27px;top:45px;">We<br>commit<br>to be <b>fit</b>.</p>
      <div class="figure-slot" role="img" aria-label="Icon of a person lifting dumbbells" style="left:155px;top:42px;width:92px;height:86px;"></div>
    </section>

    <section class="panel right-thing">
      <div class="figure-slot" role="img" aria-label="Thumbs-up hand icon" style="left:100px;top:28px;width:62px;height:70px;"></div>
      <p class="statement" style="left:0;right:0;top:124px;text-align:center;">We <b>do<br>what is<br>right</b><br>even when<br>no one is<br>watching.</p>
    </section>

    <section class="panel humor">
      <div class="figure-slot" role="img" aria-label="Smiling face icon" style="left:27px;top:52px;width:68px;height:68px;border-radius:50%;"></div>
      <p class="statement" style="right:26px;top:38px;text-align:right;">Our days are<br>brightened by a<br><b>sense of humor.</b></p>
    </section>

    <section class="panel positive">
      <p class="statement" style="left:28px;top:34px;">We look at<br>life through<br>a <b>positive</b> lens.</p>
      <svg style="position:absolute;left:268px;top:58px;" width="94" height="56" viewBox="0 0 94 56">
        <path d="M4 28 C20 6 74 6 90 28 C74 50 20 50 4 28 Z" fill="none" stroke="#fff" stroke-width="5"/>
        <circle cx="47" cy="28" r="17" fill="#fff"/>
        <circle cx="47" cy="28" r="8" fill="none" stroke="var(--navy)" stroke-width="4"/>
      </svg>
    </section>

    <div class="watermark" aria-hidden="true">
      <span style="left:172px;top:280px;">The</span>
      <span style="left:90px;top:560px;">Pruett</span>
      <span style="left:8px;top:705px;">Family</span>
    </div>
  </main>
</body>
</html>
```